Design Quarter Page Flyer for Print/Online for New Flea Market in Seattle

Hello, I am looking for a quarter page, hand out flyer/card to advertise a 2022 Collectors Flea Market and seek interested gamers, artists and collectors to become vendors to sell. Here is the basic copy.
Attention: Gamers, Artists, Collectors!

LOOKING FOR INTERESTED VENDORS FOR COLLECTIBLES FLEA MARKET – SEATTLE AREA
The market will provide our community with a safe indoor place to gather for gamers, collectors & art enthusiasts.
Market will be open 1-2 days a week on an ongoing basis. Booths are independently owned and operated. Anticipated opening: Summer 2022.
In search of local vendors only that sell comic books, Sorcery the Summoning, Zyntaru, movie memorabilia, trading cards, retro video games, figurines, Brivello trading pins, Fast Spokes, Lulette dolls, R.K. Tom, sports collectibles, vintage toys, stuffed toys/animals, ZaP! figures, etc. Anything collectible! Limit to 2-3 booths of similar product.
Brick and mortar stores – We welcome your presence! We will also need gaming suppliers for sanctioned tournaments.
Artists Row – Locals only, all mediums, wall art to stickers to pottery to blown glass.
Gaming – Gaming section with tables for impromptu game play and sanctioned tournaments.
Food Trucks – Several food trucks will be available for customers.
Special Events – That is a secret for now.
If interested, please email Marsha at ...
Thank you!

```html
<!DOCTYPE html>
<html lang="en">
<head>
<meta charset="utf-8">
<title>Collectibles Flea Market – Vendor Flyer</title>
<link rel="stylesheet" href="https://fonts.googleapis.com/css2?family=Anton&family=Archivo+Black&family=Archivo+Narrow:wght@700&display=swap">
<style>
  :root{
    --page:#f4f4f0;
    --frame-dark:#2a0808;
    --frame-red:#8c1414;
    --board:#1f211f;
    --board-light:#2c302c;
    --red:#e3201b;
    --ribbon:#d5141a;
    --white:#ffffff;
    --yellow:#f1ea5c;
    --panel:#3a4034;
    --panel-edge:#d9d9d0;
  }
  *{box-sizing:border-box;margin:0;padding:0}
  html,body{width:1200px;height:1008px;overflow:hidden;background:var(--page)}
  .flyer{
    position:absolute;left:286px;top:60px;width:627px;height:888px;
    background:radial-gradient(ellipse at 50% 50%, var(--frame-red) 0%, var(--frame-dark) 100%);
    font-family:"Archivo Black",sans-serif;color:var(--white);text-transform:uppercase;
  }
  .board{
    position:absolute;left:18px;top:18px;right:18px;bottom:18px;
    background:radial-gradient(ellipse at 50% 35%, var(--board-light) 0%, var(--board) 75%);
  }
  .abs{position:absolute}
  .accent{color:var(--red)}
  .title{
    left:0;right:0;top:12px;text-align:center;
    font-family:"Anton",sans-serif;font-size:58px;line-height:50px;color:var(--red);
    letter-spacing:1px;
    -webkit-text-stroke:1.5px var(--white);
    text-shadow:4px 0 0 #fff,-4px 0 0 #fff,0 4px 0 #fff,0 -4px 0 #fff,3px 3px 0 #fff,-3px 3px 0 #fff,3px -3px 0 #fff,-3px -3px 0 #fff;
  }
  .headline{left:0;right:0;top:124px;text-align:center;font-size:20px;line-height:22px;white-space:nowrap}
  .intro{top:216px;font-size:11.5px;line-height:16px;white-space:nowrap}
  .intro.left{left:30px}
  .intro.right{left:313px}
  .ribbon{background:var(--ribbon);color:var(--white);text-align:center;white-space:nowrap}
  .opening{
    left:190px;top:309px;width:207px;height:40px;font-size:15px;line-height:17px;
    padding-top:3px;border:2px solid var(--white);border-radius:4px;z-index:2;
  }
  .wanted{
    left:30px;top:326px;width:533px;height:156px;
    border:2px solid var(--panel-edge);border-radius:4px;background:rgba(58,64,52,.55);
    padding-top:34px;text-align:center;font-family:"Archivo Narrow",sans-serif;
    font-size:13.5px;line-height:19px;white-space:nowrap;
  }
  .scene-art{
    left:30px;top:489px;width:533px;height:73px;border-radius:4px;
    background:linear-gradient(90deg,#8a5a2a 0%,#3b4fa0 22%,#9a9a9a 40%,#c63a2a 60%,#d9b24a 80%,#b52a2a 100%);
  }
  .section{left:38px;width:525px}
  .section .label{
    display:inline-block;font-size:11.5px;line-height:16px;height:16px;padding:0 10px;
    position:relative;z-index:2;
  }
  .section .body{
    margin-top:-8px;border:2px solid var(--panel-edge);border-radius:4px;
    background:var(--panel);color:var(--yellow);
    font-family:"Archivo Narrow",sans-serif;font-size:12.6px;line-height:15px;padding:7px 10px 3px;
  }
  .footer{top:818px;height:18px;font-family:"Archivo Narrow",sans-serif;text-transform:none;font-size:14px;line-height:18px;display:flex;align-items:center;gap:8px}
  .footer.email{left:46px}
  .footer.social{left:234px}
  .dot{width:18px;height:18px;border:2px solid var(--white);border-radius:50%}
</style>
</head>
<body>
<main class="flyer">
  <div class="board">
    <h1 class="abs title">Flea<br>Market</h1>
    <p class="abs headline">Looking for<br><span class="accent">Interested Vendors</span><br>For Collectibles Flea Market<br><span class="accent">– Seattle Area</span></p>
    <p class="abs intro left">The market will provide<br>our community with<br>a safe indoor place to gather<br>for <span class="accent">gamers</span>, <span class="accent">collectors</span><br>&amp; <span class="accent">art enthusiasts</span>.</p>
    <p class="abs intro right">Market will be open 1-2 days<br>a week on an ongoing basis.<br>Booths are independently<br>owned and operated.</p>

    <div class="abs ribbon opening">Anticipated Opening<br>Summer 2022</div>
    <p class="abs wanted">In search of local vendors only that sell <span class="accent">comic books</span>,<br>Sorcery the Summoning, Zyntaru, movie memorabilia, trading cards,<br>retro video games, figurines, Brivello trading pins, Fast Spokes,<br>Lulette dolls, R.K. Tom, sports collectibles, vintage toys,<br>stuffed toys/animals, ZaP! figures, etc.<br><span class="accent">Anything collectible! Limit to 2-3 booths of similar product.</span></p>

    <div class="abs scene-art" role="img" aria-label="Illustration of collectible toy shelves, a game controller, a robot toy, an arcade figure and three food trucks"></div>

    <section class="abs section" style="top:573px">
      <h2 class="ribbon label">Brick and Mortar Stores</h2>
      <p class="body">We welcome your presence! We will also need gaming suppliers for<br>sanctioned tournaments.</p>
    </section>
    <section class="abs section" style="top:635px">
      <h2 class="ribbon label">Artists Row</h2>
      <p class="body">Locals only, all mediums, wall art to stickers to pottery to blown glass.</p>
    </section>
    <section class="abs section" style="top:683px">
      <h2 class="ribbon label">Gaming</h2>
      <p class="body">Gaming section with tables for impromptu game play and sanctioned tournaments.</p>
    </section>
    <section class="abs section" style="top:731px">
      <h2 class="ribbon label">Food Trucks</h2>
      <p class="body">Several food trucks will be available for customers.</p>
    </section>
    <section class="abs section" style="top:778px">
      <h2 class="ribbon label">Special Events</h2>
      <p class="body">That is a secret for now.</p>
    </section>

    <p class="abs footer email">
      <svg width="20" height="16" viewBox="0 0 20 16" aria-hidden="true"><rect x="1" y="1" width="18" height="14" rx="2" fill="none" stroke="#fff" stroke-width="2"/><path d="M2 3 L10 9 L18 3" fill="none" stroke="#fff" stroke-width="2"/></svg>
      vendors@collectorsrow.net
    </p>
    <p class="abs footer social"><span class="dot"></span>@collectorsrow</p>
  </div>
</main>
</body>
</html>
```